VORTIQ Business Card Design

We need a business card for a new company based on the Gold Coast, we are a new supplement distributing company called VORTIQ Sports Nutrition - Bold Horizon Sports Nutrition. We are providing new science based bodybuilding and fitness supplementation. Our company has a key focus towards next generation. We are wanting a card that is cool, innovative and fresh. We would like to see the implementation of the below image in a fresh and very innovative design that stands out. The final design should communicate New, Innovative, Cool, Science and researched based.
Target Market(s)
The target market is fitness and bodybuilder enthusiasts. Young audience so very cool looking.
Industry/Entity Type
Fitness
Contact Information for Business Card
(front of card)
VORTIQ Sports Nutrition.
Milo Harrow
CEO/Sport Nutrition Specialist
0473 628 904
Milo@vortiqfuelworks.example
www.vortiqfuelworks.example
(back of card)
Scientifically formulated supplement range
Private Nutrition consultations
comprehensive sports nutrition seminars
Requirements
Nice to have
- The card could have a cut out on one of the sides or one of the corners rounded off so the card looks different from a normal business card.
Should not have
- The colours need to complement each other and pop out.

```html
<!DOCTYPE html>
<html lang="en">
<head>
<meta charset="utf-8">
<title>VORTIQ Business Card</title>
<link href="https://fonts.googleapis.com/css2?family=Arimo:wght@400;700&family=Open+Sans:ital,wght@1,400&display=swap" rel="stylesheet">
<style>
  :root {
    --page: #ffffff;
    --card: #000000;
    --glow: #0b3b40;
    --ink-white: #ffffff;
    --ink-cyan: #5cc8ea;
    --brand-cyan: #4fc3e6;
    --brand-muted: #3e6b74;
  }
  html, body {
    margin: 0;
    padding: 0;
    width: 1200px;
    height: 740px;
    overflow: hidden;
    background: var(--page);
    font-family: "Arimo", Arial, sans-serif;
  }
  .canvas {
    position: relative;
    width: 1200px;
    height: 740px;
  }
  .card {
    position: absolute;
    top: 190px;
    width: 567px;
    height: 346px;
    background: var(--card);
    overflow: hidden;
  }
  .card--front {
    left: 30px;
    border-top-right-radius: 200px 125px;
    background: radial-gradient(ellipse 240px 170px at 200px 190px, var(--glow) 0%, rgba(0,0,0,0) 100%), var(--card);
  }
  .card--back {
    left: 605px;
    border-top-left-radius: 200px 125px;
    background: radial-gradient(ellipse 260px 200px at 385px 170px, var(--glow) 0%, rgba(0,0,0,0) 100%), var(--card);
  }
  .brand {
    position: absolute;
    left: 44px;
    top: 60px;
    display: flex;
    align-items: center;
    gap: 8px;
  }
  .brand__dot {
    width: 14px;
    height: 14px;
    border-radius: 50%;
    background: var(--brand-cyan);
  }
  .brand__name {
    font-weight: 700;
    font-size: 28px;
    letter-spacing: 1px;
    color: var(--brand-cyan);
  }
  .tagline {
    position: absolute;
    left: 24px;
    top: 152px;
    margin: 0;
    font-family: "Open Sans", Arial, sans-serif;
    font-style: italic;
    font-size: 9px;
    color: var(--ink-white);
  }
  .contact {
    position: absolute;
    right: 50px;
    top: 94px;
    margin: 0;
    text-align: right;
    font-size: 14px;
    line-height: 19px;
    color: var(--ink-cyan);
  }
  .contact__company { color: var(--ink-white); }
  .person {
    position: absolute;
    right: 50px;
    top: 256px;
    text-align: right;
  }
  .person__name {
    margin: 0;
    font-size: 17px;
    color: var(--ink-white);
  }
  .person__role {
    margin: 3px 0 0;
    font-size: 13px;
    color: var(--ink-cyan);
  }
  .services {
    position: absolute;
    right: 318px;
    top: 146px;
    margin: 0;
    padding: 0;
    list-style: none;
    text-align: right;
    font-size: 12px;
    line-height: 19.5px;
    color: var(--ink-cyan);
  }
  .brand-large {
    position: absolute;
    left: 270px;
    top: 128px;
    width: 230px;
    display: flex;
    flex-direction: column;
    align-items: center;
    gap: 18px;
  }
  .brand-large__dot {
    width: 70px;
    height: 70px;
    border-radius: 50%;
    background: var(--brand-muted);
  }
  .brand-large__name {
    font-weight: 700;
    font-size: 48px;
    letter-spacing: 2px;
    color: var(--brand-muted);
  }
</style>
</head>
<body>
<main class="canvas">
  <section class="card card--front">
    <div class="brand">
      <span class="brand__dot"></span>
      <span class="brand__name">VORTIQ</span>
    </div>
    <p class="tagline">BOLD HORIZON SPORTS NUTRITION.</p>
    <p class="contact">
      <span class="contact__company">VORTIQ Sports Nutrition</span><br>
      0473 628 904<br>
      Milo@vortiqfuelworks.example<br>
      www.vortiqfuelworks.example
    </p>
    <div class="person">
      <p class="person__name">Milo Harrow</p>
      <p class="person__role">CEO/Sport Nutrition Specialist</p>
    </div>
  </section>

  <section class="card card--back">
    <ul class="services">
      <li>Scientifically formulated supplement range</li>
      <li>Private Nutrition consultations comprehensive</li>
      <li>sports nutrition seminars</li>
    </ul>
    <div class="brand-large">
      <span class="brand-large__dot"></span>
      <span class="brand-large__name">VORTIQ</span>
    </div>
  </section>
</main>
</body>
</html>
```